Single Page Production Company Site

Clean. Simple. Minimalist site with one page.

No portfolio, just some text to communicate a general overview of what the company does.

We work for a very select group of clients, creating strong brand personalities online. The site is specifically minimal and not communicating too much about what we do.. we have a variety of capabilities to work with clients and prefer to be broad with just a simple landing page as the point of contact for our brand.
Updates

Christmas holidays are coming up, maybe people need some time away from work with family and friends... We can keep working on this and I will provide feedback as quickly as possible, but I understand if designers have other commitments during the coming days. Thanks for your hard work!

Industry/Entity Type

Design Agency

Coding

Coded - Design and coding required

Number of Pages Required

1 page

Font styles to use
Sans Serif

Requirements
Must have
• Clean, bold text headlines.
Nice to have
• Unsure about any images used in the design, would like to see options with or without.

```html
<!DOCTYPE html>
<html lang="en">
<head>
<meta charset="utf-8">
<title>Harbor Lane Studio</title>
<link rel="stylesheet" href="https://fonts.googleapis.com/css2?family=Montserrat:wght@400;500;600;700;800&family=Anton&family=Open+Sans:wght@500&display=swap">
<style>
  :root {
    --blue: #1338de;
    --yellow: #ffec1e;
    --green: #467b22;
    --pink: #e01272;
    --navy: #0d0865;
    --white: #ffffff;
  }
  * { margin: 0; padding: 0; box-sizing: border-box; }
  html, body { width: 1200px; height: 2698px; overflow: hidden; }
  body { font-family: "Montserrat", sans-serif; color: var(--white); position: relative; }
  .section { position: absolute; left: 0; width: 1200px; }
  .section--intro { top: 0; height: 675px; background: var(--blue); }
  .section--team { top: 675px; height: 675px; background: var(--green); }
  .section--about { top: 1350px; height: 674px; background: var(--pink); }
  .section--contact { top: 2024px; height: 674px; background: var(--navy); }
  .abs { position: absolute; }
  .center { left: 0; width: 1200px; text-align: center; }
  .section-title { font-weight: 600; font-size: 30px; line-height: 36px; letter-spacing: 0.3px; }
  .rule { position: absolute; left: 340px; width: 519px; height: 5px; }
  .rule--yellow { background: var(--yellow); }
  .rule--blue { background: var(--blue); }
  .rule--pink { background: var(--pink); }
  .tag {
    position: absolute; display: flex; align-items: center; justify-content: center;
    font-weight: 800; font-size: 20px; letter-spacing: 0.2px;
  }
  .tag--yellow { background: var(--yellow); color: var(--blue); left: 422px; width: 355px; height: 37px; }
  .tag--blue { background: var(--blue); color: var(--white); font-weight: 600; height: 33px; }
  .copy { font-size: 14px; line-height: 19px; text-align: center; }
  .copy--small { font-size: 10.5px; line-height: 15px; text-align: center; }
  .star { position: absolute; left: 547px; width: 106px; height: 101px; }
  .star text { font-family: "Anton", sans-serif; font-size: 20px; }
  .field-label { font-size: 19px; font-weight: 400; }
  .field-line { position: absolute; height: 2px; background: var(--pink); }
  .send-button {
    position: absolute; left: 527px; top: 2484px; width: 146px; height: 30px;
    border-radius: 15px; background: var(--pink); color: var(--white);
    font-family: "Open Sans", sans-serif; font-weight: 500; font-size: 13px;
    display: flex; align-items: center; justify-content: center;
  }
</style>
</head>
<body>

<section class="section section--intro">
  <h1 class="abs center section-title" style="top:73px;">CONCEPT. CREATE. COMPLETE.</h1>
  <div class="rule rule--yellow" style="top:108px;"></div>

  <h2 class="tag tag--yellow" style="top:150px;">DESIGN HAPPENS HERE</h2>
  <p class="abs center copy" style="top:190px;">We are leading the way in design innovation for modern websites.<br>Clean, functional, intuitive&nbsp; websites for&nbsp; progressive businesses.</p>

  <h2 class="tag tag--yellow" style="top:282px;">ART HAPPENS HERE</h2>
  <p class="abs center copy" style="top:321px;">Building brands through design, we believe that contrast is everything.<br>For industry leaders who set the pace and exceed expectations, we help give the<br>company voice and soul.</p>

  <h2 class="tag tag--yellow" style="top:426px;">IDEAS HAPPENS HERE</h2>
  <p class="abs center copy" style="top:466px;">Clients look to us for unique, exceptional solutions to their technology issues.<br>We bring creativity to the table and solve your business' problems with<br>actionable solutions.</p>

  <svg class="star" style="top:540px;" viewBox="0 0 106 101" aria-label="Click">
    <polygon points="53,0 65,38 106,38 73,62 85,101 53,78 21,101 33,62 0,38 41,38" fill="var(--yellow)"/>
    <text x="53" y="62" text-anchor="middle" fill="var(--blue)">CLICK</text>
  </svg>
</section>

<section class="section section--team">
  <h2 class="abs center section-title" style="top:51px;">THE HARBOR TEAM</h2>
  <div class="rule rule--blue" style="top:87px;"></div>
  <p class="abs copy--small" style="top:100px; left:290px; width:620px;">Harbor Lane Studio focuses on creating extraordinary online experiences for extraordinary clients. We'll work with you to create the perfect online presence for your brand.</p>

  <h3 class="tag tag--blue" style="top:157px; left:266px; width:249px;">SIZE IS EVERYTHINK</h3>
  <p class="abs copy--small" style="top:199px; left:228px; width:325px;">We don't work in a massive corporate office and we don't have a mailroom. Not that there's anything wrong with that, it's just that we like knowing each other's names, and encourage our clients to know ours. Our small staff has an advantage – our group works more efficiently, more cost-effectively and most importantly, flexible to each client's unique needs. We deliver a range of services found at any agency, with the personal service you should expect.</p>

  <h3 class="tag tag--blue" style="top:157px; left:684px; width:250px;">OUR GOAL</h3>
  <p class="abs copy--small" style="top:199px; left:645px; width:325px;">Harbor Lane Studio brings your brand to life, online. We do it all when it comes to online commerce for retail stores, wholesalers and distributors. Taking your company online introduces a world of opportunity, as well as specific challenges associated with online trade. We'll assist you in establishing a successful online presence and bringing your brand to a worldwide audience.</p>

  <h3 class="tag tag--blue" style="top:354px; left:466px; width:267px;">Who's Mark?</h3>
  <p class="abs copy--small" style="top:401px; left:338px; width:524px;">Mark Ellison, owner of Harbor Lane Studio is not your typical principal. He's worked internationally with both Northgate Media and Larkspur Press publications in photo production for titles including Metro Mode and Gilded Review. Originally from coastal Maine and an all-around New Englander, Mark can often be found sailing during the summer and skiing during winter. He believes that inspiration comes from experiencing the world, not from sitting in a cubicle. But no worries, his biggest fear is being offline, and is always within an arms reach of the Internet.</p>

  <svg class="star" style="top:540px;" viewBox="0 0 106 101" aria-label="Click">
    <polygon points="53,0 65,38 106,38 73,62 85,101 53,78 21,101 33,62 0,38 41,38" fill="var(--yellow)"/>
    <text x="53" y="62" text-anchor="middle" fill="var(--green)">CLICK</text>
  </svg>
</section>

<section class="section section--about">
  <h2 class="abs center section-title" style="top:98px;">WE GET YOU</h2>
  <div class="rule rule--yellow" style="top:134px;"></div>
  <p class="abs copy" style="top:188px; left:355px; width:490px; line-height:18.8px;">Having a website isn't enough. You need to show your customers you understand the socially connected online world we live in. We help you create designs that capture the personality of your business and project the image you want your customers to see. Maybe you're a small company looking to sell yourself in the big leagues; maybe you're a big company that wants to look approachable; either way, we can make it happen. You'll come across looking professional, unique and strikingly hip all at the same time.</p>

  <p class="abs center" style="top:443px; font-size:20px; line-height:19px;">You'll come across looking professional, unique and<br>strikingly hip all at the same time.</p>

  <svg class="star" style="top:540px;" viewBox="0 0 106 101" aria-label="Click">
    <polygon points="53,0 65,38 106,38 73,62 85,101 53,78 21,101 33,62 0,38 41,38" fill="var(--yellow)"/>
    <text x="53" y="62" text-anchor="middle" fill="var(--pink)">CLICK</text>
  </svg>
</section>

<section class="section section--contact">
  <h2 class="abs center section-title" style="top:62px;">CONTACT US</h2>
  <div class="rule rule--pink" style="top:118px;"></div>
</section>

<form class="contact-form">
  <label class="abs field-label" style="left:229px; top:2251px;">Name</label>
  <div class="field-line" style="left:229px; top:2293px; width:312px;"></div>
  <label class="abs field-label" style="left:658px; top:2251px;">Mail Address</label>
  <div class="field-line" style="left:658px; top:2293px; width:313px;"></div>
  <label class="abs field-label" style="left:229px; top:2319px;">Type your message here...</label>
  <div class="field-line" style="left:229px; top:2421px; width:742px;"></div>
  <div class="send-button">Send Message</div>
</form>

<svg class="abs" style="left:536px; top:2566px;" width="128" height="80" viewBox="0 0 128 80" aria-label="Scroll down">
  <polyline points="10,10 64,67 118,10" fill="none" stroke="var(--white)" stroke-width="11" stroke-linecap="round" stroke-linejoin="round"/>
</svg>

</body>
</html>
```